Verdanix Medical Business Card

Create a high class Business card for Medical Aesthetics and Wellness Practice called Verdanix Medical Aesthetics and Wellness as per the logo attached.
Addresss is: 418 Harlan Brook Road Suite 312 Harrowfield, New York 11093
Phone (555)204-7391 IG @verdanix_medical
Verdanixmedical.example

I need 5 different name configurations
1) Dr. Theo Valcourt
Aesthetics and Wellness Specialist
Medical Director

2) Rosalind Pettinger, NP
Clinical Nurse Manager

3) Marla Vostrik, RN
Aesthetic Nurse Specialist

4) Petra Halvesen, RN

5) Dana Kowbeck, L.E.
Senior Licensed Esthetician

Target Market(s)

22-55 Females

Industry/Entity Type

Medical Spa and Wellness

Contact Information for Business Card

Logo, address, phone, web, instagram, providers name

Requirements
Must have
• Attractive classy modern look

```html
<!DOCTYPE html>
<html lang="en">
<head>
<meta charset="utf-8">
<title>Verdanix Medical Business Card</title>
<link rel="stylesheet" href="https://fonts.googleapis.com/css2?family=Bodoni+Moda:wght@400&family=Marcellus&display=swap">
<style>
  :root {
    --backdrop: #3a3a3a;
    --card-white: #ffffff;
    --card-black: #1b1b1b;
    --ink: #222222;
    --strip: #2b2b2b;
    --accent-blue: #2e9fc7;
    --paper-text: #f4f4f4;
  }
  * { margin: 0; padding: 0; box-sizing: border-box; }
  html, body {
    width: 1200px; height: 800px; overflow: hidden;
    background: var(--backdrop);
  }
  .canvas {
    position: relative; width: 1200px; height: 800px;
    display: flex; align-items: center; justify-content: center; gap: 50px;
  }
  .card {
    position: relative; width: 525px; height: 300px;
    border-radius: 34px; overflow: hidden;
    box-shadow: 0 18px 40px rgba(0,0,0,0.35);
  }
  .card--back { background: var(--card-white); color: var(--ink); }
  .card--front { background: var(--card-black); color: var(--paper-text); }

  .brand { position: absolute; text-align: center; }
  .brand__name {
    font-family: "Bodoni Moda", serif; font-weight: 400;
    letter-spacing: 0.12em; line-height: 1;
  }
  .brand__tagline {
    font-family: "Marcellus", serif; letter-spacing: 0.06em;
    text-transform: uppercase; margin-top: 8px;
  }
  .brand__region {
    font-family: "Marcellus", serif; letter-spacing: 0.7em;
    text-transform: uppercase; margin-top: 6px;
  }

  .card--back .brand { left: 0; width: 250px; top: 118px; }
  .card--back .brand__name { font-size: 38px; }
  .card--back .brand__tagline { font-size: 9.5px; }
  .card--back .brand__region { font-size: 7px; }

  .divider-strip {
    position: absolute; left: 250px; top: 0; width: 18px; height: 100%;
    background: var(--strip);
    display: flex; flex-direction: column; align-items: center;
    justify-content: flex-end; gap: 4px; padding-bottom: 36px;
  }
  .divider-strip svg { width: 11px; height: 11px; }

  .providers { position: absolute; left: 288px; top: 28px; width: 220px; }
  .provider { margin-bottom: 7px; }
  .provider__name {
    font-family: "Marcellus", serif; font-size: 12.5px; line-height: 1.15;
  }
  .provider__role {
    font-family: "Marcellus", serif; font-size: 7.5px; line-height: 1.25;
    color: var(--accent-blue); letter-spacing: 0.02em;
  }

  .contact {
    position: absolute; left: 288px; bottom: 30px;
    font-family: "Marcellus", serif; font-size: 10px; line-height: 1.4;
    font-style: normal;
  }

  .card--front .brand { left: 0; width: 100%; top: 92px; }
  .card--front .brand__name { font-size: 54px; }
  .card--front .brand__tagline { font-size: 12.5px; margin-top: 10px; }
  .card--front .brand__region { font-size: 8.5px; margin-top: 8px; }

  .social {
    position: absolute; left: 0; width: 100%; bottom: 40px;
    display: flex; justify-content: center; align-items: center; gap: 8px;
    font-family: "Marcellus", serif; font-size: 12px; letter-spacing: 0.03em;
  }
  .social__dot {
    width: 11px; height: 11px; border: 1.2px solid var(--paper-text); border-radius: 50%;
  }
</style>
</head>
<body>
<main class="canvas">
  <section class="card card--back" aria-label="Business card, contact side">
    <div class="brand">
      <div class="brand__name">Verdanix</div>
      <div class="brand__tagline">Medical Aesthetics and Wellness</div>
      <div class="brand__region">New York</div>
    </div>

    <div class="divider-strip">
      <svg viewBox="0 0 12 12" aria-label="Phone" role="img">
        <path d="M3 1.5 L4.6 1.5 L5.4 3.8 L4.2 4.8 Q5.2 7 7.2 7.8 L8.2 6.6 L10.5 7.4 L10.5 9 Q10 10.5 8.5 10.5 Q2 9.5 1.5 3.5 Q1.5 1.8 3 1.5 Z" fill="none" stroke="#fff" stroke-width="0.9"/>
      </svg>
      <svg viewBox="0 0 12 12" aria-label="Website" role="img">
        <circle cx="6" cy="6" r="4.6" fill="none" stroke="#fff" stroke-width="0.9"/>
        <ellipse cx="6" cy="6" rx="2" ry="4.6" fill="none" stroke="#fff" stroke-width="0.8"/>
        <line x1="1.4" y1="6" x2="10.6" y2="6" stroke="#fff" stroke-width="0.8"/>
      </svg>
      <svg viewBox="0 0 12 12" aria-label="Address" role="img">
        <path d="M6 11 Q2 6.5 2 4.6 A4 4 0 0 1 10 4.6 Q10 6.5 6 11 Z" fill="none" stroke="#fff" stroke-width="0.9"/>
        <circle cx="6" cy="4.6" r="1.4" fill="none" stroke="#fff" stroke-width="0.8"/>
      </svg>
    </div>

    <div class="providers">
      <div class="provider">
        <div class="provider__name">Dr. Theo Valcourt</div>
        <div class="provider__role">Aesthetics and Wellness Specialist<br>Medical Director</div>
      </div>
      <div class="provider">
        <div class="provider__name">Rosalind Pettinger, NP</div>
        <div class="provider__role">Clinical Nurse Manager</div>
      </div>
      <div class="provider">
        <div class="provider__name">Marla Vostrik, RN</div>
        <div class="provider__role">Aesthetic Nurse Specialist</div>
      </div>
      <div class="provider">
        <div class="provider__name">Petra Halvesen, RN</div>
        <div class="provider__role">Aesthetic Nurse Specialist</div>
      </div>
      <div class="provider">
        <div class="provider__name">Dana Kowbeck, L.E.</div>
        <div class="provider__role">Senior Licensed Esthetician</div>
      </div>
    </div>

    <address class="contact">
      (555)204-7391<br>
      Verdanixmedical.example<br>
      418 Harlan Brook Road<br>
      Suite 312 Harrowfield, New York 11093
    </address>
  </section>

  <section class="card card--front" aria-label="Business card, brand side">
    <div class="brand">
      <div class="brand__name">Verdanix</div>
      <div class="brand__tagline">Medical Aesthetics and Wellness</div>
      <div class="brand__region">New York</div>
    </div>
    <div class="social">
      <span class="social__dot"></span>
      <span>@verdanix_medical</span>
    </div>
  </section>
</main>
</body>
</html>
```